Claimant Aid Pathway USA - Email Marketing Creative

Looking for design of email creative for Claimant Aid Pathway USA website. Call to action based email focused on conveying brand, messaging of "Disabled? Unable to Work? You May Qualify for Social Security Disability Benefits", call to action of 'Free Evaluation' or 'Fast, Free, No Obligation Evaluation'. Can use any messaging from the current mock of https://lnkshrt.example/7QwXpR4 . Please focus on imaging of 50+ people if used, red white and blue coloring (patriotic) yet USA looking. Creative must be done in HTML as well as text for easy use and include Email Opt Out link etc. Examples of competitors emails attached. PLEASE DO NOT COPY them. Just use as examples.

Target Market(s)

Disabled American. Age 50+ Looking for help applying, re-applying or handling a social security disability hearing.

Industry/Entity Type

Legal

Font styles to use
Serif
Sans Serif

Colors

Designer to choose colors to be used in the design.

Requirements
Must have
• call to action based html
Nice to have
• strong call to action.
Should not have
• Should not be cookie cutter. Stick to simple yet official looking.

```html
<!DOCTYPE html>
<html lang="en">
<head>
<meta charset="utf-8">
<title>Claimant Aid Pathway USA – Free Evaluation</title>
<link rel="stylesheet" href="https://fonts.googleapis.com/css2?family=Source+Sans+3:wght@300;400;600;700&display=swap">
<style>
  :root {
    --page-bg: #e9e9e9;
    --card-bg: #ffffff;
    --panel-bg: #f1f4fc;
    --navy: #13183a;
    --ink: #111111;
    --ink-muted: #555555;
    --red: #ee1c25;
    --box-dark: #0d0e26;
    --rule: #cfcfcf;
    --sand: #d8d2c6;
    --sea: #b9c3c6;
  }
  * { box-sizing: border-box; margin: 0; padding: 0; }
  html, body {
    width: 868px; height: 1200px; overflow: hidden;
    background: var(--page-bg);
    font-family: "Source Sans 3", Arial, sans-serif;
    color: var(--ink);
  }
  .email { position: relative; width: 868px; height: 1200px; }
  .hero-card {
    position: absolute; left: 20px; top: 17px; width: 828px; height: 784px;
    background: var(--card-bg); border: 1px solid #dcdcdc;
  }
  .brand-bar {
    height: 145px; display: flex; align-items: center; justify-content: center; gap: 16px;
  }
  .brand-dot { width: 64px; height: 64px; border-radius: 50%; background: var(--red); }
  .brand-name { font-weight: 700; font-size: 34px; color: var(--navy); letter-spacing: 0.5px; }
  .hero-photo {
    position: relative; height: 345px;
    background: linear-gradient(180deg, #e6e8e6 0%, var(--sea) 38%, #e4e0d8 55%, var(--sand) 100%);
  }
  .hero-headline {
    position: absolute; left: 51px; top: 112px;
    font-weight: 400; font-size: 50px; line-height: 52px; color: #0c0c0c;
  }
  .offer-panel { height: 293px; background: var(--panel-bg); text-align: center; position: relative; }
  .offer-lead {
    position: absolute; left: 0; right: 0; top: 36px;
    font-size: 35px; font-weight: 400; color: #444; line-height: 44px;
  }
  .offer-lead strong { font-weight: 700; color: var(--ink); }
  .offer-program {
    position: absolute; left: 144px; top: 86px; width: 534px; height: 63px;
    background: var(--box-dark); color: #fff;
    font-size: 34px; line-height: 63px; font-weight: 400;
  }
  .cta-button {
    position: absolute; left: 208px; top: 175px; width: 413px; height: 76px;
    background: var(--red); color: #fff; border-radius: 38px;
    font-size: 40px; font-weight: 600; line-height: 76px; text-decoration: none;
  }
  .about { position: absolute; left: 43px; top: 840px; width: 779px; }
  .about-title { font-size: 18.5px; font-weight: 700; margin-bottom: 12px; }
  .about-copy {
    font-size: 15.3px; line-height: 20.8px; text-align: justify; color: #1a1a1a;
  }
  .footer-rule {
    position: absolute; left: 20px; top: 1103px; width: 828px; height: 1px; background: var(--rule);
  }
  .footer-note {
    position: absolute; left: 0; right: 0; top: 1122px; text-align: center;
    font-size: 13.5px; font-weight: 300; color: var(--ink-muted);
  }
  .footer-note a { color: var(--ink-muted); text-decoration: underline; }
</style>
</head>
<body>
<div class="email">
  <section class="hero-card">
    <header class="brand-bar">
      <span class="brand-dot"></span>
      <span class="brand-name">Claimant Aid Pathway USA</span>
    </header>
    <div class="hero-photo" role="img" aria-label="Photo of an older couple in sun hats walking along a sandy beach by the sea">
      <h1 class="hero-headline">Disabled?<br>Unable to Work?</h1>
    </div>
    <div class="offer-panel">
      <p class="offer-lead">You May <strong>Qualify</strong> for</p>
      <p class="offer-program">Social Security Disability Benefits</p>
      <a class="cta-button" href="https://lnkshrt.example/7QwXpR4">Free Evaluation</a>
    </div>
  </section>

  <section class="about">
    <h2 class="about-title">What is Claimant Aid Pathway USA?</h2>
    <p class="about-copy">Claimant Aid Pathway USA is an independent service that helps people through the Social Security Disability Insurance (SSDI) process. SSDI is a federal program run by the Social Security Administration (SSA) and funded through Social Security payroll taxes. It supports people who can no longer hold steady work because of a lasting medical condition, and in some cases members of their family. We do not pay benefits and are not affiliated with the SSA; we help you prepare your application, reapply after a denial or get ready for a hearing. To qualify, you generally need enough work credits from years of paying Social Security taxes and must meet the SSA definition of disability: you cannot do the work you did before, you cannot adjust to other work because of your condition, and the condition is expected to last at least one year or result in death. Find out today whether you may qualify.</p>
  </section>

  <div class="footer-rule"></div>
  <p class="footer-note">2019 claimantaidpathwayusa.example. All Rights Reserved. &middot; <a href="https://claimantaidpathwayusa.example/unsubscribe">Unsubscribe</a></p>
</div>
</body>
</html>
```